SKYVANTIX (drone photo and video) and Photogrammetry Services (mapping and 3D modeling)

We need a business card design for a SKYVANTIX. Our businesses provides (drone) Aerial Photo and Video Captures. However we also provide Photogrammetry (which is 3D modeling and mapping). We greatly value unique points of view taken of landscapes and subjects with aerial photography and videography. 3D modeling and mapping is the other area of focus and have an incredibly broad scope of applications and imaginative creativity.

Target Market(s)

Based out of Northern Virginia and serving the greater Virginia and Maryland areas

Industry/Entity Type

Drone Photo and video and Photogrammetry Services (mapping and 3D modeling)

Contact Information for Business Card

3D Models, Maps and Photo/Video Production name: Marcus Pellerin email: mtp@skyvantix.us website: skyvantix.us phone: 571-389-6043; please also include "Aerial Photo/Video and 3D Mapping/Modeling"

Requirements
Must have
• Please make this design vertical and double sided. The selection box is not letting me choose Double Sided but that is my wish. Incorporate uploaded LOGO and color scheme
Nice to have
• Preferably does not feel too crowded and balances not having an exaggerated amount of distracting detail
Should not have
• do not cram bullet points or text in long form

```html
<!DOCTYPE html>
<html lang="en">
<head>
<meta charset="utf-8">
<title>SKYVANTIX Business Card</title>
<link href="https://fonts.googleapis.com/css2?family=Arimo:wght@400;700&display=swap" rel="stylesheet">
<style>
  :root {
    --page-bg: #e6e6e6;
    --card-white: #ffffff;
    --card-dark: #262626;
    --card-dark-2: #3a3a3a;
    --ink: #3b3b3b;
    --ink-soft: #6b6b6b;
    --orange: #f39a1a;
    --orange-deep: #ee6a1c;
    --red: #e5262c;
    --divider: #d4d4d4;
  }
  * { box-sizing: border-box; margin: 0; padding: 0; }
  html, body {
    width: 1200px; height: 802px; overflow: hidden;
    background: var(--page-bg);
    font-family: "Arimo", Arial, sans-serif;
  }
  .sheet {
    width: 1200px; height: 802px;
    display: flex; align-items: center; justify-content: center; gap: 90px;
  }
  .card {
    position: relative;
    width: 310px; height: 540px;
    overflow: hidden;
    box-shadow: 0 6px 18px rgba(0,0,0,0.18);
  }

  /* Front */
  .card-front {
    background: var(--card-white);
    display: flex; flex-direction: column; align-items: center;
    padding: 62px 24px 0;
  }
  .brand {
    display: flex; flex-direction: column; align-items: center; gap: 14px;
  }
  .brand-dot {
    width: 58px; height: 58px; border-radius: 50%;
    background: linear-gradient(135deg, var(--orange), var(--red));
  }
  .brand-name {
    font-weight: 700; font-size: 32px; letter-spacing: 2px; line-height: 1;
    white-space: nowrap;
  }
  .card-front .brand-name { color: var(--ink); }
  .tagline {
    margin-top: 14px;
    color: var(--ink-soft); font-size: 11px; letter-spacing: 0.2px;
    white-space: nowrap; text-align: center;
  }
  .person { margin-top: 48px; text-align: center; }
  .person-name {
    color: var(--orange-deep); font-weight: 700; font-size: 19px;
    text-transform: uppercase; letter-spacing: 0.5px; white-space: nowrap;
  }
  .person-role { color: var(--ink-soft); font-size: 13px; margin-top: 5px; }
  .divider {
    width: 150px; height: 1px; background: var(--divider);
    margin: 24px 0 20px;
  }
  .contacts {
    list-style: none; color: var(--ink-soft); font-size: 14px;
  }
  .contacts li { display: flex; align-items: center; gap: 10px; height: 26px; white-space: nowrap; }
  .contacts svg { width: 14px; height: 14px; flex: none; }
  .address {
    margin-top: 22px;
    color: var(--ink-soft); font-size: 13px; text-align: center;
  }
  .edge-band {
    position: absolute; left: 0; right: 0; bottom: 0; height: 9px;
    background: linear-gradient(90deg, var(--orange), var(--red));
  }

  /* Back */
  .card-back { background: var(--card-dark); }
  .back-pattern {
    position: absolute; inset: 0;
    background: linear-gradient(150deg, #1b1b1b 0%, var(--card-dark) 45%, var(--card-dark-2) 75%, #4a4a4a 100%);
  }
  .brand-back {
    position: absolute; left: 50%; top: 50%; transform: translate(-50%, -50%);
  }
  .card-back .brand-name { color: #ffffff; font-size: 34px; }
</style>
</head>
<body>
<main class="sheet">
  <section class="card card-front" aria-label="Card front">
    <div class="brand">
      <span class="brand-dot"></span>
      <span class="brand-name">SKYVANTIX</span>
    </div>
    <p class="tagline">Aerial Photo/Video and 3D Mapping/Modeling</p>
    <div class="person">
      <p class="person-name">Marcus Pellerin</p>
      <p class="person-role">Manager</p>
    </div>
    <div class="divider"></div>
    <ul class="contacts">
      <li>
        <svg viewBox="0 0 16 16"><circle cx="8" cy="8" r="8" fill="#ee6a1c"/><path d="M5 4.5c.5-.5 1.2-.3 1.4.2l.6 1.3c.2.4 0 .8-.3 1l-.5.4c.4 1 1.2 1.8 2.2 2.2l.4-.5c.3-.3.7-.4 1-.3l1.3.6c.5.2.7.9.2 1.4-1.5 1.5-4 .2-5.4-1.4C4.6 8 3.5 6 5 4.5z" fill="#fff"/></svg>
        571-389-6043
      </li>
      <li>
        <svg viewBox="0 0 16 16"><rect x="1" y="3" width="14" height="10" rx="1" fill="#ee6a1c"/><path d="M1.5 3.8 8 9l6.5-5.2" fill="none" stroke="#fff" stroke-width="1.3"/></svg>
        mtp@skyvantix.us
      </li>
      <li>
        <svg viewBox="0 0 16 16"><circle cx="8" cy="8" r="7" fill="#e5262c"/><circle cx="8" cy="8" r="3" fill="none" stroke="#fff" stroke-width="1.3"/><path d="M1 8h14M8 1v14" stroke="#fff" stroke-width="0.8"/></svg>
        skyvantix.us
      </li>
    </ul>
    <p class="address">Leesburg, VA 20175</p>
    <div class="edge-band"></div>
  </section>

  <section class="card card-back" aria-label="Card back">
    <div class="back-pattern" role="img" aria-label="Embossed repeating pattern of round mountain emblems on dark stock"></div>
    <div class="brand brand-back">
      <span class="brand-dot"></span>
      <span class="brand-name">SKYVANTIX</span>
    </div>
  </section>
</main>
</body>
</html>
```